Fitness Business Card Design Needed

We are looking for a business card design that stands out but is also simple and unique. I like the idea of on one side using the picture of myself with my logo at my feet. I love the texture on the business card so please take that into account when designing. Then on the other side having my contact details. I want it to be clean, modern, and pretty. I am open to designs that allow spot gloss or gold foiling.

Contact Information for Business Card

Space for Name, Phone number, email, and website

```html
<!DOCTYPE html>
<html lang="en">
<head>
<meta charset="utf-8">
<title>Northlight Studio – Business Cards</title>
<link href="https://fonts.googleapis.com/css2?family=Montserrat:wght@500;600&family=Roboto:wght@400;500&display=swap" rel="stylesheet">
<style>
  :root {
    --backdrop: #2a2a2c;
    --card: #ffffff;
    --ink: #3a3a3c;
    --ink-soft: #5a5a5e;
    --gold: #b0823a;
    --gold-light: #e2b860;
    --gold-deep: #9c7026;
    --rule: #c9c9c9;
    --skin: #c98a6a;
    --swim: #e2553f;
    --sand: #cbb08a;
  }
  * { box-sizing: border-box; margin: 0; padding: 0; }
  html, body { width: 1200px; height: 801px; overflow: hidden; }
  body {
    background: var(--backdrop);
    font-family: "Roboto", Arial, sans-serif;
    color: var(--ink);
    position: relative;
  }
  .card {
    position: absolute;
    width: 540px;
    height: 309px;
    background: var(--card);
    overflow: hidden;
  }
  .card--portrait { left: 40px; top: 246px; }
  .card--contact { left: 620px; top: 246px; }

  /* studio name */
  .studio-name {
    position: absolute;
    display: flex;
    align-items: center;
    justify-content: center;
    gap: 8px;
    white-space: nowrap;
    font-family: "Montserrat", Arial, sans-serif;
    font-weight: 500;
    font-size: 18px;
    color: var(--ink);
  }
  .studio-name__mark {
    width: 9px; height: 9px;
    background: var(--gold);
    flex: none;
  }
  .card--contact .studio-name { left: 20px; width: 240px; top: 142px; }
  .card--portrait .studio-name { left: 150px; width: 240px; top: 250px; }

  /* contact side */
  .divider {
    position: absolute;
    left: 272px; top: 60px;
    width: 1px; height: 170px;
    background: var(--rule);
  }
  .details {
    position: absolute;
    left: 296px; top: 62px;
    right: 16px;
  }
  .details__name {
    font-family: "Montserrat", Arial, sans-serif;
    font-weight: 600;
    font-size: 22px;
    color: var(--gold);
    letter-spacing: 0.3px;
  }
  .details__role {
    font-size: 14px;
    letter-spacing: 0.5px;
    color: var(--ink);
    margin-top: 2px;
  }
  .details__address {
    font-size: 13px;
    color: var(--ink-soft);
    margin-top: 12px;
    line-height: 1.4;
  }
  .details__list { list-style: none; margin-top: 10px; }
  .details__item {
    display: flex; align-items: center; gap: 8px;
    font-size: 13px;
    color: var(--ink-soft);
    line-height: 1.5;
    white-space: nowrap;
  }
  .details__item svg { width: 11px; height: 11px; fill: var(--gold); flex: none; }
  .foil-band {
    position: absolute;
    left: 0; right: 0; bottom: 0;
    height: 10px;
    border-top: 2px solid #555;
    background: linear-gradient(90deg, var(--gold-deep), var(--gold-light) 60%, var(--gold-deep));
  }

  /* portrait side */
  .portrait {
    position: absolute;
    left: 215px; top: 32px;
    width: 110px; height: 205px;
    background: linear-gradient(180deg, #d9c39a 0%, var(--skin) 25%, var(--swim) 45%, var(--skin) 60%, var(--sand) 100%);
    border-radius: 50px 50px 14px 14px;
  }
</style>
</head>
<body>
  <section class="card card--portrait" aria-label="Portrait side">
    <div class="portrait" role="img" aria-label="Full-length photo of the trainer standing on a mound of sand"></div>
    <p class="studio-name"><span class="studio-name__mark"></span>Northlight Studio</p>
  </section>

  <section class="card card--contact" aria-label="Contact side">
    <p class="studio-name"><span class="studio-name__mark"></span>Northlight Studio</p>
    <div class="divider"></div>
    <div class="details">
      <p class="details__name">LENA MORALES</p>
      <p class="details__role">FITNESS TRAINER</p>
      <p class="details__address">1420 Willow Crest Road<br>Juneau, Alaska 99801</p>
      <ul class="details__list">
        <li class="details__item">
          <svg viewBox="0 0 24 24"><path d="M6.6 10.8a15 15 0 0 0 6.6 6.6l2.2-2.2c.3-.3.7-.4 1-.2 1.1.4 2.3.6 3.6.6.6 0 1 .4 1 1V20c0 .6-.4 1-1 1A17 17 0 0 1 3 4c0-.6.4-1 1-1h3.5c.6 0 1 .4 1 1 0 1.3.2 2.5.6 3.6.1.3 0 .7-.2 1z"/></svg>
          555 203 7718
        </li>
        <li class="details__item">
          <svg viewBox="0 0 24 24"><path d="M2 5h20v14H2z M2 5l10 8 10-8"/></svg>
          info@northlightstudio.com
        </li>
        <li class="details__item">
          <svg viewBox="0 0 24 24"><circle cx="12" cy="12" r="10"/></svg>
          www.northlightstudio.com
        </li>
      </ul>
    </div>
    <div class="foil-band"></div>
  </section>
</body>
</html>
```